Business Card Design

We have recently seen two business cards that caught our attention and think the designs would work for us. We are an accounting firm that serves small businesses in a variety of industries. Attached are the two business card that inspired us along with very rough layouts. We would like to see a professional layout using our company information.

Industry/Entity Type

Accounting

Contact Information for Business Card

Company Name - Porter Lyle
Address - 4120 Marbury Lane, Suite 310, Houston, TX 77058
713-555-0186 - Main
281-555-0143 - Fax

Team Member Names, emails and phone numbers (see attachment)

```html
<!DOCTYPE html>
<html lang="en">
<head>
<meta charset="utf-8">
<title>Porter Lyle — Business Card</title>
<link href="https://fonts.googleapis.com/css2?family=Lato:wght@400;700;900&display=swap" rel="stylesheet">
<style>
  :root {
    --backdrop: #e9e6e1;
    --card: #ffffff;
    --ink: #111111;
    --muted: #7a7a7a;
    --mark: #b9b9b9;
  }
  * { margin: 0; padding: 0; box-sizing: border-box; }
  html, body {
    width: 1200px;
    height: 1023px;
    overflow: hidden;
    background: var(--backdrop);
    font-family: "Lato", Arial, sans-serif;
  }
  .stage {
    width: 1200px;
    height: 1023px;
    display: flex;
    align-items: center;
    justify-content: center;
  }
  .card {
    position: relative;
    width: 500px;
    height: 875px;
    background: var(--card);
    box-shadow: 0 6px 24px rgba(0,0,0,0.12);
  }
  .brand {
    position: absolute;
    top: 170px;
    left: 0;
    right: 0;
    display: flex;
    align-items: center;
    justify-content: center;
    gap: 18px;
  }
  .brand-square {
    width: 30px;
    height: 30px;
    background: var(--mark);
  }
  .brand-name {
    font-size: 46px;
    font-weight: 900;
    letter-spacing: 4px;
    text-transform: uppercase;
    color: var(--ink);
  }
  .details {
    position: absolute;
    left: 48px;
    top: 420px;
    right: 40px;
  }
  .person-name {
    font-size: 34px;
    font-weight: 900;
    color: var(--ink);
    text-transform: uppercase;
    letter-spacing: 0.5px;
  }
  .person-title {
    font-size: 23px;
    color: var(--muted);
    margin-top: 2px;
  }
  .address {
    font-size: 23px;
    color: var(--muted);
    line-height: 1.25;
    margin-top: 26px;
  }
  .contacts {
    list-style: none;
    margin-top: 22px;
  }
  .contact {
    display: flex;
    align-items: center;
    gap: 12px;
    font-size: 23px;
    line-height: 1.25;
    color: var(--muted);
  }
  .contact svg {
    width: 20px;
    height: 20px;
    flex: none;
    fill: var(--ink);
  }
</style>
</head>
<body>
<main class="stage">
  <article class="card">
    <div class="brand">
      <span class="brand-square"></span>
      <span class="brand-name">Porter Lyle</span>
    </div>

    <section class="details">
      <h1 class="person-name">Dana Whitford</h1>
      <p class="person-title">Account Manager</p>
      <p class="address">4120 Marbury Lane, Suite 310<br>Houston, TX 77058</p>
      <ul class="contacts">
        <li class="contact">
          <svg viewBox="0 0 20 20" aria-hidden="true"><path d="M5 2 Q2 3 2 7 Q4 14 13 18 Q17 18 18 15 L14 12 L12 14 Q8 12 6 8 L8 6 Z"/></svg>
          713-555-0186 (Office)
        </li>
        <li class="contact">
          <svg viewBox="0 0 20 20" aria-hidden="true"><path d="M5 2 Q2 3 2 7 Q4 14 13 18 Q17 18 18 15 L14 12 L12 14 Q8 12 6 8 L8 6 Z"/></svg>
          713-555-0172 (Direct)
        </li>
        <li class="contact">
          <svg viewBox="0 0 20 20" aria-hidden="true"><path d="M6 1 H14 Q16 1 16 3 V17 Q16 19 14 19 H6 Q4 19 4 17 V3 Q4 1 6 1 Z M6 4 V15 H14 V4 Z"/></svg>
          832-555-0119
        </li>
        <li class="contact">
          <svg viewBox="0 0 20 20" aria-hidden="true"><path d="M1 4 H19 V16 H1 Z M2.5 5.5 L10 11 L17.5 5.5 Z"/></svg>
          dwhitford@porterlyle.com
        </li>
      </ul>
    </section>
  </article>
</main>
</body>
</html>
```